I want to sell a virtual ticket that captures customers details.

Using this information, i manually write the customers details on a piece of paper and enter them into a draw/raffle to potentially win a watch. I dont need random generators/software to pick winners, as law mandates this process to be physically done. All i need is a nice website that allows customers to purchase and enter. I have posted a few links below in the description. If you refer to orvanteltrading.com, you will see what i am after. I have my own site www.thekestrelmarque.com.au but i dont like how it looks and i want something better. I hope this will give you an idea on what i am after.

Target Market(s)

adults aged approximately 24-56

Industry/Entity Type

luxury watches / contestant giveaways

Number of Pages Required

4 page

Font styles to use
Serif
Other font styles liked:
• something classy - i am not sure

Colors

Designer to choose only greyscale colors for use in the design.

Requirements
Must have
• Stripe payment software

```html
<!DOCTYPE html>
<html lang="en">
<head>
<meta charset="utf-8">
<title>The Kestrel Marque</title>
<link href="https://fonts.googleapis.com/css2?family=Fira+Sans:wght@300;400;500;600;700&family=Merriweather:wght@300;400;700&display=swap" rel="stylesheet">
<style>
:root{
  --accent:#7a7a7a;
  --accent-soft:#9a9a9a;
  --ink:#111111;
  --text:#333333;
  --muted:#666666;
  --band:#f2f2f2;
  --white:#ffffff;
}
*{box-sizing:border-box;margin:0;padding:0}
html,body{width:1200px;height:2876px;overflow:hidden}
body{position:relative;background:var(--white);font-family:"Fira Sans",sans-serif;color:var(--text)}
.abs{position:absolute}
.serif{font-family:"Merriweather",serif}

/* header */
.latest{left:150px;top:42px;font-size:13px;color:var(--ink)}
.brand{left:480px;top:36px;width:240px;text-align:center;font-weight:500;font-size:15px;letter-spacing:1.5px;color:var(--ink);text-transform:uppercase;display:flex;align-items:center;justify-content:center;gap:8px}
.brand .dot{width:14px;height:14px;background:var(--ink)}
.nav{right:150px;top:42px;display:flex;gap:26px;font-size:16px;font-weight:500;color:var(--ink)}
.nav .active{color:var(--accent)}

/* hero */
.hero-photo{left:0;top:100px;width:1200px;height:503px}
.hero-title{left:150px;top:188px;font-size:41px;line-height:55px;color:var(--ink);font-weight:400}
.hero-sub{left:150px;top:306px;font-size:16px;color:var(--ink)}
.btn-accent{background:var(--accent);color:var(--white);font-size:13px;font-weight:500;display:flex;align-items:center;justify-content:center;letter-spacing:.5px}
.subscribe{left:150px;top:356px;width:142px;height:42px}
.countdown{left:150px;top:429px;width:415px;height:82px;background:var(--ink);display:flex;align-items:center}
.cd-cell{width:106px;text-align:center;color:var(--white);font-family:"Merriweather",serif;border-right:1px solid #555;height:48px;display:flex;flex-direction:column;justify-content:center}
.cd-cell:last-child{border-right:none}
.cd-num{font-size:21px;line-height:24px}
.cd-unit{font-size:15px}
.tickets{left:570px;top:429px;width:105px;height:82px;background:var(--white);display:flex;flex-direction:column;align-items:center;justify-content:center;font-family:"Merriweather",serif;color:var(--ink)}

/* about */
.about-photo{left:173px;top:700px;width:322px;height:360px;background:radial-gradient(ellipse at 45% 55%,#6f6f6f 0%,#959595 45%,#b3b3b3 100%);border:1px solid #888}
.frame-line{background:var(--ink)}
.about-title{left:583px;top:668px;font-size:35px;color:var(--ink);font-weight:400}
.about-text{left:583px;top:726px;width:478px;font-size:14px;line-height:22.5px;color:var(--ink)}
.about-text p{margin-bottom:22.5px}
.btn-outline{left:583px;top:1042px;width:169px;height:42px;border:2px solid var(--accent);color:var(--accent);font-size:13px;display:flex;align-items:center;justify-content:center;gap:6px}

/* values */
.values{left:0;top:1160px;width:1200px;height:487px;background:var(--band)}
.sec-title{font-family:"Merriweather",serif;font-size:35px;color:var(--ink);font-weight:400;text-align:center}
.value-label{font-size:20px;font-weight:700;color:var(--ink);letter-spacing:.3px}
.values-watch{left:556px;top:1296px;width:166px;height:300px;background:linear-gradient(180deg,#8c8c8c 0%,#3c3c3c 35%,#222 50%,#3c3c3c 65%,#8c8c8c 100%);border-radius:40px}

/* how to play */
.how-sub{left:0;top:1770px;width:1200px;text-align:center;font-size:19px;font-weight:500;color:var(--ink)}
.step-label{width:300px;text-align:center;font-size:20px;font-weight:500;color:var(--ink)}

/* packages */
.card{width:208px;height:337px;top:2208px;background:var(--white);box-shadow:0 2px 10px rgba(0,0,0,.07);text-align:center}
.card-head{height:52px;color:var(--white);font-weight:600;font-size:15px;display:flex;flex-direction:column;align-items:center;justify-content:center;position:relative;line-height:18px}
.card-head small{font-size:13px;font-weight:500}
.card-head::after{content:"";position:absolute;left:50%;bottom:-7px;margin-left:-6px;border:6px solid transparent;border-top-color:inherit;border-bottom:0;border-top-width:7px}
.head-dark{background:var(--ink);border-color:var(--ink)}
.head-accent{background:var(--accent);border-color:var(--accent)}
.price{margin-top:30px;font-size:52px;font-weight:700;color:var(--ink);line-height:56px}
.entries{margin-top:32px;font-size:14px;color:var(--muted);display:flex;align-items:center;justify-content:center;gap:6px}
.tick{width:13px;height:13px;border-radius:50%;display:inline-flex;align-items:center;justify-content:center}
.divider{margin:24px auto 0;width:160px;height:1px;background:#333}
.cause{margin-top:26px;font-size:14px;color:var(--muted)}
.enter{margin:26px auto 0;width:186px;height:42px;font-size:14px;font-weight:500;color:var(--white);display:flex;align-items:center;justify-content:center}
.popular{left:500px;top:2198px;width:74px;height:22px;background:var(--ink);color:var(--white);font-size:12px;display:flex;align-items:center;justify-content:center}

/* footer */
.footer{left:0;top:2620px;width:1200px;height:215px;background:var(--band)}
.foot-title{font-size:16px;font-weight:500;color:var(--ink)}
.foot-links{font-size:14px;color:var(--text);line-height:27px}
.foot-brand{left:150px;top:2700px;font-size:15px;font-weight:500;letter-spacing:1.5px;color:var(--ink);text-transform:uppercase;display:flex;align-items:center;gap:8px}
.foot-brand .dot{width:14px;height:14px;background:var(--ink)}
.social{top:2751px;width:30px;height:30px;border-radius:50%;background:var(--accent)}
.news-form{left:824px;top:2760px;width:226px;height:38px;border:1px solid #999;background:var(--white);display:flex}
.news-form span{flex:1;font-size:12px;color:#444;display:flex;align-items:center;padding-left:12px}
.news-form .send{width:44px;background:var(--accent);display:flex;align-items:center;justify-content:center}
.copyright{left:0;top:2835px;width:1200px;height:41px;background:var(--ink);color:#ddd;font-size:13px;display:flex;align-items:center;justify-content:center}
</style>
</head>
<body>

<!-- header -->
<div class="abs latest">Latest Winners</div>
<div class="abs brand"><span class="dot"></span>The Kestrel Marque</div>
<nav class="abs nav"><span class="active">Home</span><span>FAQ</span><span>Contact US</span></nav>

<!-- hero -->
<svg class="abs hero-photo" viewBox="0 0 1200 503" width="1200" height="503" role="img" aria-label="Luxury diver's watch on a dark background">
  <defs>
    <radialGradient id="heroGlow" cx="0.6" cy="0.45" r="0.6">
      <stop offset="0" stop-color="#2e2e2e"/>
      <stop offset="1" stop-color="#151515"/>
    </radialGradient>
  </defs>
  <polygon points="533,0 1200,0 1200,450 562,450" fill="url(#heroGlow)"/>
  <polygon points="562,450 1200,450 1200,503 570,503" fill="#000"/>
</svg>
<h1 class="abs hero-title serif">Your Chance to Win<br>Starts here.</h1>
<div class="abs hero-sub">Supporting Health &amp; Making Wealth</div>
<div class="abs subscribe btn-accent">SUBSCRIBE&nbsp;&nbsp;→</div>
<div class="abs countdown">
  <div class="cd-cell"><span class="cd-num">1</span><span class="cd-unit">days</span></div>
  <div class="cd-cell"><span class="cd-num">10</span><span class="cd-unit">hours</span></div>
  <div class="cd-cell"><span class="cd-num">34</span><span class="cd-unit">min</span></div>
  <div class="cd-cell"><span class="cd-num">21</span><span class="cd-unit">Sec</span></div>
</div>
<div class="abs tickets"><span style="font-size:21px">91</span><span style="font-size:15px">tickets left</span></div>

<!-- about -->
<div class="abs frame-line" style="left:150px;top:677px;width:193px;height:2px"></div>
<div class="abs frame-line" style="left:150px;top:677px;width:2px;height:198px"></div>
<div class="abs frame-line" style="left:516px;top:887px;width:2px;height:198px"></div>
<div class="abs frame-line" style="left:324px;top:1083px;width:194px;height:2px"></div>
<div class="abs about-photo" role="img" aria-label="Chronograph wristwatch resting on a wooden table"></div>
<h2 class="abs about-title serif">About Us</h2>
<div class="abs about-text">
  <p>We are a group of friends from Melbourne, Australia who all share a common passion – a love for watches. We aim to provide an equal opportunity for all watches lovers in Australia, whilst, more importantly, paving the way for a cleaner, eco-friendlier world.</p>
  <p>We strongly believe that all communities, regardless of interests, should share a common goal, which is why we have joined forces with (TO BE CONFIRMED), whose main aim is to help plant trees across Australia to prevent deforestation in our backyard.</p>
  <p>Our services are one of a kind, as each package sold goes towards planting trees in the much-needed regions of Australia. We hope you are excited as we are, as we embark on this journey together!</p>
</div>
<div class="abs btn-outline">OUR PACKAGES →</div>

<!-- values -->
<div class="abs values"></div>
<h2 class="abs sec-title" style="left:0;top:1188px;width:1230px">Our Values</h2>
<div class="abs values-watch" role="img" aria-label="Steel diver's watch with dark dial"></div>
<svg class="abs" style="left:0;top:1160px" width="1200" height="487" viewBox="0 0 1200 487" fill="none" stroke="#111">
  <g stroke-width="1.5">
    <line x1="349" y1="175" x2="486" y2="175"/>
    <line x1="768" y1="175" x2="906" y2="175"/>
    <line x1="349" y1="417" x2="486" y2="417"/>
    <line x1="768" y1="417" x2="906" y2="417"/>
  </g>
  <g stroke-width="1.5" stroke-dasharray="12 10">
    <line x1="486" y1="175" x2="578" y2="245"/>
    <line x1="768" y1="175" x2="696" y2="232"/>
    <line x1="486" y1="417" x2="578" y2="344"/>
    <line x1="768" y1="417" x2="696" y2="352"/>
  </g>
  <g stroke="#7a7a7a" stroke-width="1.6">
    <rect x="258" y="128" width="8" height="22"/>
    <rect x="304" y="128" width="8" height="22"/>
    <path d="M266 132 l14 -6 l12 4 l12 -2 M266 146 l10 4 l14 -12 l8 8 M280 126 l10 14 l6 -4"/>
    <path d="M954 126 h14 l16 16 l-14 14 l-16 -16 z"/>
    <circle cx="961" cy="133" r="2"/>
    <path d="M970 147 c-4 -4 2 -8 4 -4 c2 -4 8 0 4 4 l-4 4 z"/>
    <circle cx="258" cy="387" r="12"/>
    <path d="M258 379 v8 l6 4"/>
    <circle cx="953" cy="377" r="7"/>
    <path d="M942 398 c0 -10 6 -13 11 -13 c4 0 7 1 9 3"/>
    <path d="M966 386 l8 3 v6 c0 5 -4 7 -8 9 c-4 -2 -8 -4 -8 -9 v-6 z"/>
  </g>
</svg>
<div class="abs value-label" style="left:244px;top:1323px">RESPECT</div>
<div class="abs value-label" style="left:929px;top:1323px">LOYALTY</div>
<div class="abs value-label" style="left:190px;top:1565px">COMMITMENT</div>
<div class="abs value-label" style="left:929px;top:1565px">TRUST</div>

<!-- how to play -->
<h2 class="abs sec-title" style="left:0;top:1720px;width:1200px">How to Play</h2>
<div class="abs how-sub">IT'S THAT SIMPLE!</div>
<svg class="abs" style="left:0;top:1830px" width="1200" height="160" viewBox="0 0 1200 160">
  <line x1="150" y1="27" x2="1050" y2="27" stroke="#111" stroke-width="2"/>
  <path d="M446 21 l6 6 l-6 6 M746 21 l6 6 l-6 6" fill="none" stroke="#111" stroke-width="1.6"/>
  <g font-family="Fira Sans, sans-serif" font-size="12" font-weight="700" text-anchor="middle" fill="#fff">
    <circle cx="300" cy="27" r="13" fill="#111"/><text x="300" y="31">1</text>
    <circle cx="600" cy="27" r="13" fill="#111"/><text x="600" y="31">2</text>
    <circle cx="900" cy="27" r="13" fill="#111"/><text x="900" y="31">3</text>
  </g>
  <g fill="none" stroke="#7a7a7a" stroke-width="1.6">
    <rect x="277" y="81" width="46" height="46" rx="3"/>
    <path d="M283 90 h34 M285 96 l6 4 l6 -4 l6 4 l6 -4 l6 4 M283 106 h34 v14 h-34 z M283 113 h34 M295 106 v14"/>
    <path d="M580 82 h14 v18 h24 v28 h-38 z M594 82 l24 18"/>
    <path d="M586 108 h10 M586 116 h14 M604 108 h8 M604 116 h8 M586 94 h4"/>
    <path d="M886 82 h28 v12 c0 9 -6 16 -14 16 c-8 0 -14 -7 -14 -16 z M886 86 h-12 c0 8 5 12 12 12 M914 86 h12 c0 8 -5 12 -12 12 M900 110 v10 M890 126 h20 l-3 -6 h-14 z"/>
    <path d="M900 88 l2 4 l4 1 l-3 3 l1 4 l-4 -2 l-4 2 l1 -4 l-3 -3 l4 -1 z"/>
  </g>
</svg>
<div class="abs step-label" style="left:150px;top:1998px">Enter Details</div>
<div class="abs step-label" style="left:450px;top:1998px">Choose a Package</div>
<div class="abs step-label" style="left:750px;top:1998px">Wait for Draw</div>

<!-- packages -->
<h2 class="abs sec-title" style="left:0;top:2096px;width:1200px">Our Package</h2>

<div class="abs card" style="left:150px">
  <div class="card-head head-dark">BRONZE</div>
  <div class="price">$7</div>
  <div class="entries"><span class="tick" style="background:#333"><svg width="8" height="8" viewBox="0 0 8 8"><path d="M1 4 l2 2 l4 -4" stroke="#fff" stroke-width="1.5" fill="none"/></svg></span>1 Entry</div>
  <div class="divider"></div>
  <div class="cause">Help with other supplies</div>
  <div class="enter" style="background:var(--ink)">Enter the Competition</div>
</div>
<div class="abs card" style="left:382px">
  <div class="card-head head-accent">SILVER</div>
  <div class="price">$12</div>
  <div class="entries"><span class="tick" style="background:var(--accent)"><svg width="8" height="8" viewBox="0 0 8 8"><path d="M1 4 l2 2 l4 -4" stroke="#fff" stroke-width="1.5" fill="none"/></svg></span>2 Entries</div>
  <div class="divider"></div>
  <div class="cause">Help build a Koala's Home</div>
  <div class="enter" style="background:var(--accent)">Enter the Competition</div>
</div>
<div class="abs popular">Popular</div>
<div class="abs card" style="left:614px">
  <div class="card-head head-dark">GOLD</div>
  <div class="price">$16</div>
  <div class="entries"><span class="tick" style="background:var(--ink)"><svg width="8" height="8" viewBox="0 0 8 8"><path d="M1 4 l2 2 l4 -4" stroke="#fff" stroke-width="1.5" fill="none"/></svg></span>3 Entries</div>
  <div class="divider"></div>
  <div class="cause">Help us fight deforestation</div>
  <div class="enter" style="background:var(--ink)">Enter the Competition</div>
</div>
<div class="abs card" style="left:845px">
  <div class="card-head head-accent">DELUXE<small>Fan favourite + Best odds</small></div>
  <div class="price">$19</div>
  <div class="entries"><span class="tick" style="background:var(--accent)"><svg width="8" height="8" viewBox="0 0 8 8"><path d="M1 4 l2 2 l4 -4" stroke="#fff" stroke-width="1.5" fill="none"/></svg></span>5 Entries</div>
  <div class="divider"></div>
  <div class="cause">Help plant a tree</div>
  <div class="enter" style="background:var(--accent)">Enter the Competition</div>
</div>
<svg class="abs" style="left:928px;top:2175px" width="42" height="32" viewBox="0 0 42 32">
  <path d="M3 10 l10 8 l8 -15 l8 15 l10 -8 l-4 16 h-28 z" fill="#555555"/>
  <rect x="7" y="28" width="28" height="4" fill="#555555"/>
</svg>

<!-- footer -->
<div class="abs footer"></div>
<div class="abs foot-brand"><span class="dot"></span>The Kestrel Marque</div>
<div class="abs social" style="left:151px" aria-label="Social link"></div>
<div class="abs social" style="left:196px" aria-label="Social link"></div>
<div class="abs social" style="left:241px" aria-label="Social link"></div>

<div class="abs foot-title" style="left:403px;top:2657px">Quick Links</div>
<div class="abs foot-links" style="left:403px;top:2695px">FAQs<br>Contact Us<br>Terms &amp; Conditions</div>

<div class="abs foot-title" style="left:643px;top:2657px">Packages</div>
<div class="abs foot-links" style="left:643px;top:2695px">Bronze<br>Silver<br>Gold<br>Deluxe</div>

<div class="abs foot-title" style="left:824px;top:2657px">Newsletter</div>
<div class="abs foot-links" style="left:824px;top:2695px;width:210px;line-height:20px">Subscribe to our newsletter to get updates about contest.</div>
<div class="abs news-form"><span>Enter Your Email Address</span><div class="send"><svg width="16" height="16" viewBox="0 0 16 16"><path d="M1 8 l14 -7 l-4 14 l-3 -5 z" fill="#fff"/></svg></div></div>

<div class="abs copyright">© 2021 The Kestrel Marque | All Rights Reserved</div>

</body>
</html>
```